Buch-/eBook-Cover für professionelles Finanzbuch
Zielgruppe
Selbstständig in der Finanzaufklärung als Speaker und Verkäufer von Sachwerten
Aufgabenstellung
soll ein professionelles Finanzbuch sein von der Optik mit Foto von Technologiemetallen /Seltenen Erden

```html
<!DOCTYPE html>
<html lang="de">
<head>
<meta charset="utf-8">
<title>Zukunftschance Industrierohstoffe und kostbare Metalle – Buchcover</title>
<link rel="stylesheet" href="https://fonts.googleapis.com/css2?family=Oswald:wght@400;500;600;700&display=swap">
<style>
  :root {
    --page-bg: #ffffff;
    --cover-black: #0b0b0b;
    --cover-black-soft: #171615;
    --gold-light: #f6e4ae;
    --gold-mid: #d2ab62;
    --gold-deep: #8c6a2e;
    --ink-dark: #1a140b;
  }
  html, body {
    margin: 0;
    padding: 0;
    width: 930px;
    height: 1200px;
    overflow: hidden;
    background: var(--page-bg);
  }
  .canvas {
    position: relative;
    width: 930px;
    height: 1200px;
  }
  .book-cover {
    position: absolute;
    left: 95px;
    top: 30px;
    width: 740px;
    height: 1140px;
    display: block;
    box-shadow: 0 10px 30px rgba(0,0,0,0.25);
  }
  .cover-text {
    font-family: "Oswald", "Arial Narrow", sans-serif;
  }
  .kicker { font-weight: 400; font-size: 30px; letter-spacing: 4px; }
  .title-top { font-weight: 600; font-size: 92px; }
  .connector { font-weight: 500; font-size: 28px; letter-spacing: 2px; }
  .title-main { font-weight: 600; font-size: 240px; }
  .subtitle { font-weight: 400; font-size: 25px; letter-spacing: 2px; }
  .author { font-weight: 600; font-size: 34px; letter-spacing: 3px; }
</style>
</head>
<body>
<div class="canvas">
  <svg class="book-cover" viewBox="0 0 740 1140" xmlns="http://www.w3.org/2000/svg">
    <defs>
      <linearGradient id="cover-bg" x1="0" y1="0" x2="0" y2="1">
        <stop offset="0" stop-color="var(--cover-black-soft)"/>
        <stop offset="1" stop-color="var(--cover-black)"/>
      </linearGradient>
      <linearGradient id="gold-text" x1="0" y1="0" x2="0" y2="1">
        <stop offset="0" stop-color="var(--gold-light)"/>
        <stop offset="0.55" stop-color="var(--gold-mid)"/>
        <stop offset="1" stop-color="var(--gold-deep)"/>
      </linearGradient>
      <linearGradient id="gold-band" x1="0" y1="0" x2="1" y2="0">
        <stop offset="0" stop-color="var(--gold-deep)"/>
        <stop offset="0.45" stop-color="var(--gold-light)"/>
        <stop offset="1" stop-color="var(--gold-mid)"/>
      </linearGradient>
      <linearGradient id="photo-tones" x1="0" y1="0" x2="1" y2="1">
        <stop offset="0" stop-color="#0d1420"/>
        <stop offset="0.3" stop-color="#2a5878"/>
        <stop offset="0.55" stop-color="#6b3b20"/>
        <stop offset="0.8" stop-color="#b07a3a"/>
        <stop offset="1" stop-color="#1a120b"/>
      </linearGradient>
      <linearGradient id="photo-fade" x1="0" y1="0" x2="0" y2="1">
        <stop offset="0" stop-color="#0b0b0b" stop-opacity="1"/>
        <stop offset="0.35" stop-color="#0b0b0b" stop-opacity="0.2"/>
        <stop offset="1" stop-color="#0b0b0b" stop-opacity="0.3"/>
      </linearGradient>
    </defs>

    <rect class="cover-background" width="740" height="1140" fill="url(#cover-bg)"/>

    <g class="title-block cover-text" fill="url(#gold-text)">
      <line x1="40" y1="52" x2="80" y2="52" stroke="var(--gold-mid)" stroke-width="3"/>
      <line x1="660" y1="52" x2="700" y2="52" stroke="var(--gold-mid)" stroke-width="3"/>
      <text class="kicker" x="370" y="63" text-anchor="middle" fill="var(--gold-light)">ZUKUNFTSCHANCE</text>

      <text class="title-top" x="30" y="162" textLength="680" lengthAdjust="spacingAndGlyphs">INDUSTRIEROHSTOFFE</text>

      <line x1="30" y1="176" x2="710" y2="176" stroke="var(--gold-mid)" stroke-width="3"/>
      <line x1="30" y1="197" x2="330" y2="197" stroke="var(--gold-mid)" stroke-width="2"/>
      <line x1="410" y1="197" x2="710" y2="197" stroke="var(--gold-mid)" stroke-width="2"/>
      <text class="connector" x="370" y="208" text-anchor="middle">UND</text>

      <text class="title-main" x="20" y="425" textLength="700" lengthAdjust="spacingAndGlyphs">KOSTBARE</text>
      <text class="title-main" x="20" y="640" textLength="700" lengthAdjust="spacingAndGlyphs">METALLE</text>
    </g>

    <g class="subtitle-band">
      <rect x="0" y="652" width="740" height="60" fill="url(#gold-band)"/>
      <text class="cover-text subtitle" x="370" y="691" text-anchor="middle" fill="var(--ink-dark)">VOM UNBEKANNTEN ZUM UNENTBEHRLICHEN</text>
    </g>

    <g class="cover-photo" role="img" aria-label="Foto: Glasbehälter mit glänzenden Metallen und Rohstoffen auf dunkler, spiegelnder Fläche">
      <rect x="0" y="712" width="740" height="331" fill="url(#photo-tones)"/>
      <rect x="0" y="712" width="740" height="331" fill="url(#photo-fade)"/>
    </g>

    <g class="author-band">
      <rect x="0" y="1043" width="740" height="97" fill="url(#gold-band)"/>
      <text class="cover-text author" x="370" y="1100" text-anchor="middle" fill="var(--ink-dark)">LENA HARWIG</text>
    </g>
  </svg>
</div>
</body>
</html>
```